Pediatric Pelvic Health Brochure

Looking to design a brochure for Marlow Brook's pelvic health program. I can provide imagery once I see the layout. Our website is marlowbrookpt.example so the look should reflect that

If you see PDF titled blue and word doc you will see what we provided as thoguhts.

Target Market(s)

parents of children

Industry/Entity Type

Health And Wellness

Font styles to use
Serif

Requirements
Must have
• clear call outs - easy to read with copy,
Should not have
• not look bland or dated

```html
<!DOCTYPE html>
<html lang="en">
<head>
<meta charset="utf-8">
<title>Marlow Brook — Pediatric Pelvic Health Brochure</title>
<link href="https://fonts.googleapis.com/css2?family=Libre+Baskerville:wght@400;700&family=Roboto:ital,wght@0,300;0,400;0,500;0,700;1,400&display=swap" rel="stylesheet">
<style>
  :root {
    --navy: #12409a;
    --navy-deep: #0f3a8f;
    --cyan: #10bdf0;
    --cyan-bright: #0fb8ee;
    --white: #ffffff;
    --ink: #1d2a44;
    --photo-light: #dcebf7;
    --photo-mid: #a9c6e4;
  }
  * { margin: 0; padding: 0; box-sizing: border-box; }
  html, body { width: 1200px; height: 848px; overflow: hidden; background: var(--white); }
  .brochure { position: relative; width: 1200px; height: 848px; overflow: hidden; font-family: "Roboto", Arial, sans-serif; }
  .backdrop { position: absolute; inset: 0; }
  .serif { font-family: "Libre Baskerville", Georgia, serif; }

  .diagnoses-title { position: absolute; left: 34px; top: 34px; }
  .diagnoses-title .lead { display: block; color: var(--cyan); font-size: 31px; font-weight: 700; letter-spacing: 4px; line-height: 1; }
  .diagnoses-title .sub { display: block; color: var(--white); font-size: 15.5px; font-weight: 700; letter-spacing: 2.4px; margin-top: 8px; }

  .diagnosis-list { position: absolute; left: 34px; width: 330px; list-style: none; font-weight: 300; font-size: 14px; line-height: 17px; }
  .diagnosis-list li { position: relative; padding-left: 15px; margin-bottom: 10px; }
  .diagnosis-list li::before { content: ""; position: absolute; left: 0; top: 5px; width: 7px; height: 7px; border-radius: 50%; background: var(--cyan); }
  .diagnosis-list.on-navy { top: 116px; color: var(--white); }
  .diagnosis-list.on-navy li.spaced { margin-bottom: 15px; }
  .diagnosis-list.on-white { top: 512px; color: var(--ink); }

  .contact { position: absolute; left: 400px; width: 400px; top: 0; text-align: center; color: var(--white); }
  .contact-title { margin-top: 34px; font-size: 30px; font-weight: 700; letter-spacing: 4px; }
  .consult-offer { margin: 44px auto 0; width: 290px; font-style: italic; font-size: 21.5px; line-height: 27px; }
  .contact-icon { display: block; margin: 0 auto; }
  .icon-phone { margin-top: 36px; }
  .phone-number { margin-top: 10px; font-size: 28px; font-weight: 700; letter-spacing: 0.5px; }
  .icon-pin { margin-top: 56px; }
  .address { margin-top: 16px; font-size: 21px; line-height: 27px; }
  .address strong { font-weight: 700; }

  .brand { position: absolute; left: 800px; width: 400px; top: 562px; display: flex; justify-content: center; align-items: center; gap: 10px; }
  .brand-mark { width: 22px; height: 22px; background: var(--navy); }
  .brand-name { color: var(--navy); font-size: 26px; font-weight: 400; }

  .program-title { position: absolute; left: 800px; width: 400px; top: 626px; text-align: center; font-weight: 700; line-height: 1; }
  .program-title .line-one { display: block; color: var(--navy-deep); font-size: 37px; }
  .program-title .line-two { display: block; color: var(--cyan); font-size: 37px; margin-top: 6px; }
  .audience { position: absolute; left: 800px; width: 400px; top: 718px; text-align: center; color: var(--ink); font-size: 15px; font-weight: 300; }
  .website { position: absolute; left: 880px; width: 240px; top: 800px; text-align: center; color: var(--white); font-size: 17px; letter-spacing: 2px; }
</style>
</head>
<body>
<main class="brochure">
  <svg class="backdrop" width="1200" height="848" viewBox="0 0 1200 848" aria-hidden="false">
    <defs>
      <linearGradient id="familyPhotoTone" x1="0" y1="0" x2="1" y2="1">
        <stop offset="0" stop-color="#e8f1fa"/>
        <stop offset="0.5" stop-color="#c9dcef"/>
        <stop offset="1" stop-color="#eef3f8"/>
      </linearGradient>
      <linearGradient id="heartPhotoTone" x1="0" y1="0" x2="1" y2="1">
        <stop offset="0" stop-color="#f1f3f6"/>
        <stop offset="0.6" stop-color="#e2e6ec"/>
        <stop offset="1" stop-color="#f6f7f9"/>
      </linearGradient>
    </defs>

    <!-- left panel -->
    <path class="diagnoses-band" d="M0 0 H400 V436 C330 458 250 488 175 486 C95 484 35 452 0 420 Z" fill="var(--navy)"/>
    <path d="M0 628 C130 620 260 660 362 848" fill="none" stroke="var(--cyan)" stroke-width="3"/>
    <path d="M0 676 C130 664 270 710 350 848" fill="none" stroke="var(--cyan)" stroke-width="3"/>
    <path role="img" aria-label="Photo: clinician in a white coat holding a red heart" d="M0 690 C120 680 250 720 332 848 H0 Z" fill="url(#heartPhotoTone)"/>
    <circle cx="168" cy="674" r="12" fill="var(--navy)"/>

    <!-- middle panel -->
    <path class="contact-band" d="M400 0 H800 V624 C720 628 660 660 600 690 C540 720 480 732 400 712 Z" fill="var(--cyan)"/>

    <!-- right panel -->
    <path class="cover-band" d="M800 0 H1200 V537 C1100 545 1000 520 940 470 C880 420 840 400 800 390 Z" fill="var(--navy)"/>
    <path role="img" aria-label="Photo: smiling doctor with a clipboard beside a mother and daughter" d="M885 0 H1200 V478 C1100 470 1000 440 935 360 C870 280 858 150 885 0 Z" fill="url(#familyPhotoTone)"/>
    <path d="M830 5 C815 50 812 110 814 160" fill="none" stroke="var(--cyan)" stroke-width="3"/>
    <path d="M885 5 C855 40 843 110 841 158" fill="none" stroke="var(--cyan)" stroke-width="3"/>
    <path d="M820 205 C830 300 880 390 950 430 C1030 470 1120 480 1200 478" fill="none" stroke="var(--cyan)" stroke-width="3"/>
    <path d="M844 205 C850 290 895 370 960 410" fill="none" stroke="var(--cyan)" stroke-width="3"/>
    <circle cx="830" cy="182" r="12" fill="var(--white)"/>
    <path class="web-band" d="M690 848 C800 800 900 770 1000 770 C1100 770 1160 800 1200 848 Z" fill="var(--cyan-bright)"/>
  </svg>

  <section class="panel-diagnoses">
    <h2 class="diagnoses-title serif">
      <span class="lead">WE TREAT A</span>
      <span class="sub">RANGE OF DIAGNOSES</span>
    </h2>
    <ul class="diagnosis-list on-navy">
      <li>Constipation</li>
      <li>Increased urinary frequency</li>
      <li>Decreased urinary frequency</li>
      <li>Day-time incontinence</li>
      <li>Night-time incontinence,</li>
      <li>bed-wetting, or enuresis</li>
      <li>Giggle incontinence</li>
      <li class="spaced">Incontinence in the athletic female child or teenager</li>
      <li class="spaced">Waking up in the night to urinate or nocturia</li>
      <li>Difficulty with urination: straining, slow flow, pain during or after urination</li>
    </ul>
    <ul class="diagnosis-list on-white">
      <li>Reduced sensation of bladder or bowel fullness</li>
      <li>Pain in the abdomen, bladder or lower back</li>
      <li>Fecal incontinence</li>
      <li>Treatment after pediatric pelvic surgeries</li>
    </ul>
  </section>

  <section class="contact">
    <h2 class="contact-title serif">CONTACT US</h2>
    <p class="consult-offer">We offer a FREE 15 minute consultation to help you determine if therapy is right for you.</p>
    <svg class="contact-icon icon-phone" width="82" height="82" viewBox="0 0 82 82" aria-hidden="true">
      <path d="M41 4 A37 37 0 1 1 6 30" fill="none" stroke="var(--white)" stroke-width="2.5"/>
      <circle cx="41" cy="41" r="32" fill="var(--white)"/>
      <path d="M30 27 c2-2 4-2 5 0 l3 6 c1 2 0 3-1 4 l-2 2 c2 4 5 7 9 9 l2-2 c1-1 2-2 4-1 l6 3 c2 1 2 3 0 5 l-3 3 c-3 3-9 1-15-4 c-6-5-10-11-10-16 c0-3 1-5 2-6 z" fill="var(--cyan)"/>
    </svg>
    <p class="phone-number">555.204.1800</p>
    <svg class="contact-icon icon-pin" width="82" height="82" viewBox="0 0 82 82" aria-hidden="true">
      <path d="M41 4 A37 37 0 1 1 6 30" fill="none" stroke="var(--white)" stroke-width="2.5"/>
      <circle cx="41" cy="41" r="32" fill="var(--white)"/>
      <path d="M41 23 c-8 0-13 6-13 13 c0 8 13 24 13 24 s13-16 13-24 c0-7-5-13-13-13 z" fill="var(--cyan)"/>
      <circle cx="41" cy="36" r="5" fill="var(--white)"/>
    </svg>
    <p class="address">48 Harbor Lane<br>Ground Floor Brookfield,<br><strong>NY 10099</strong></p>
  </section>

  <section class="cover">
    <div class="brand">
      <span class="brand-mark"></span>
      <span class="brand-name serif">Marlow Brook</span>
    </div>
    <h1 class="program-title serif">
      <span class="line-one">PEDIATRIC</span>
      <span class="line-two">PELVIC HEALTH</span>
    </h1>
    <p class="audience">Treating Infants, Children &amp; Adolescents</p>
    <p class="website">marlowbrookpt.example</p>
  </section>
</main>
</body>
</html>
```